Marlow Ridge Crest Oak Realty yard sign Logo

UPDATE Design logo for Realty yard sign. 24x24 diamond or 36x24 Rectangle.
Open to all ideas. We are a discount firm but want to project a high end feel. We provide 100% of all services and extensive marketing for 1/2 the fee.
The following info must be on sign
BRIGHT PATH CREST (OR 1/3) OAK REALTY
Tomas Reyne 555-0147
CrestoakQX.com

Target Market(s)

home sellers and buyers

Industry/Entity Type

Real Estate yard sign please see sign attached in gif

Logo Text

Bright Path Crest Oak Realty OR (1/3 IN PLACE OF CREST)

Requirements
Must have
• BRIGHT PATH CREST (OR 1/3) OAK REALTY Tomas Reyne 555-0147 CrestoakQX.com FOR SALE (optional)

```html
<!DOCTYPE html>
<html lang="en">
<head>
<meta charset="utf-8">
<title>Marlow Ridge Crest Oak Realty – Yard Sign</title>
<link href="https://fonts.googleapis.com/css2?family=Montserrat:wght@500;600;700;800;900&display=swap" rel="stylesheet">
<style>
  :root {
    --page-bg: #eef0f2;
    --sign-blue: #3d4f9e;
    --sign-white: #ffffff;
    --sign-edge: #141414;
    --agent-ink: #1e3d52;
    --phone-ink: #2e3a8c;
    --brand-ink: #24407a;
    --icon-gold: #f2c230;
  }
  * { margin: 0; padding: 0; box-sizing: border-box; }
  html, body {
    width: 1200px; height: 1200px; overflow: hidden;
    background: var(--page-bg);
    font-family: "Montserrat", sans-serif;
  }
  .sign {
    position: relative;
    width: 1200px; height: 1200px;
  }
  .sign-shape { position: absolute; inset: 0; }
  .sign-text {
    position: absolute; left: 0; width: 1200px;
    text-align: center; line-height: 1;
    transform: translateY(-50%);
    white-space: nowrap;
  }
  .for-label {
    top: 222px; font-size: 38px; font-weight: 600;
    color: var(--sign-white); letter-spacing: 1px;
  }
  .sale-label {
    font-family: "Montserrat", sans-serif;
    font-size: 80px; font-weight: 800; letter-spacing: 3px;
  }
  .brand-name {
    top: 590px; font-size: 60px; font-weight: 800;
    color: var(--brand-ink); line-height: 1.15;
  }
  .agent-name {
    top: 789px; font-size: 48px; font-weight: 700;
    color: var(--agent-ink); letter-spacing: 1px;
  }
  .agent-phone {
    top: 860px; font-size: 82px; font-weight: 900;
    color: var(--phone-ink); letter-spacing: 1px;
  }
  .website {
    top: 940px; font-size: 32px; font-weight: 500;
    color: var(--sign-white);
  }
  .phone-icon {
    position: absolute; left: 572px; top: 982px;
    width: 56px; height: 48px;
  }
</style>
</head>
<body>
  <main class="sign">
    <svg class="sign-shape" width="1200" height="1200" viewBox="0 0 1200 1200">
      <defs>
        <clipPath id="diamond-clip">
          <polygon points="600,100 1100,600 600,1100 100,600"/>
        </clipPath>
        <filter id="outlined-letters" x="-10%" y="-20%" width="120%" height="140%">
          <feMorphology in="SourceAlpha" operator="erode" radius="3" result="inner"/>
          <feFlood flood-color="#3d4f9e" result="blue"/>
          <feComposite in="blue" in2="inner" operator="in" result="innerFill"/>
          <feMerge>
            <feMergeNode in="SourceGraphic"/>
            <feMergeNode in="innerFill"/>
          </feMerge>
        </filter>
      </defs>
      <g clip-path="url(#diamond-clip)">
        <rect class="band-top" x="0" y="0" width="1200" height="354" fill="var(--sign-blue)"/>
        <rect class="band-middle" x="0" y="354" width="1200" height="544" fill="var(--sign-white)"/>
        <rect class="band-bottom" x="0" y="898" width="1200" height="302" fill="var(--sign-blue)"/>
      </g>
      <polygon class="sign-edge" points="600,100 1100,600 600,1100 100,600"
               fill="none" stroke="var(--sign-edge)" stroke-width="7" stroke-linejoin="miter"/>
      <text class="sale-label" x="600" y="325" text-anchor="middle"
            fill="var(--sign-white)" filter="url(#outlined-letters)">SALE</text>
    </svg>

    <div class="sign-text for-label">FOR</div>

    <div class="sign-text brand-name">Marlow Ridge<br>Crest Oak Realty</div>

    <div class="sign-text agent-name">TOMAS REYNE</div>
    <div class="sign-text agent-phone">555-0147</div>
    <div class="sign-text website">CrestoakQX.com</div>

    <svg class="phone-icon" viewBox="0 0 56 48" role="img" aria-label="Telephone">
      <path d="M4 16 C4 6 52 6 52 16 L52 20 L40 20 L40 14 C34 11 22 11 16 14 L16 20 L4 20 Z" fill="var(--icon-gold)"/>
      <path d="M18 18 L38 18 L50 42 C50 45 48 46 46 46 L10 46 C8 46 6 45 6 42 Z" fill="var(--icon-gold)"/>
      <g fill="var(--sign-blue)">
        <circle cx="22" cy="28" r="2"/><circle cx="28" cy="28" r="2"/><circle cx="34" cy="28" r="2"/>
        <circle cx="22" cy="34" r="2"/><circle cx="28" cy="34" r="2"/><circle cx="34" cy="34" r="2"/>
        <circle cx="22" cy="40" r="2"/><circle cx="28" cy="40" r="2"/><circle cx="34" cy="40" r="2"/>
      </g>
    </svg>
  </main>
</body>
</html>
```